" a empresa trabalha na area de divulgação, e marketing usando a ferramenta instagram e facebook, usando o perfil de seus clientes, transformando em e-commerce, é tambem atua na area de vendas de paineis de led em acrilico "

```html
<!DOCTYPE html>
<html lang="pt-BR">
<head>
<meta charset="UTF-8">
<title>Cartão de visita – Rafael Moreira</title>
<link rel="stylesheet" href="https://fonts.googleapis.com/css2?family=Montserrat:wght@500;600&family=Varela+Round&display=swap">
<style>
  :root {
    --page-bg: #e4e7eb;
    --card-bg: #f1f3f5;
    --band-dark: #3b3c40;
    --accent-red: #d62a3c;
    --accent-magenta: #b0124e;
    --name-start: #7a1f6e;
    --name-end: #e8a21a;
    --title: #b8871a;
    --text: #2f3035;
  }
  html, body {
    margin: 0;
    width: 1200px;
    height: 1200px;
    overflow: hidden;
    background: var(--page-bg);
  }
  .business-card {
    position: absolute;
    left: 100px;
    top: 320px;
    width: 1000px;
    height: 560px;
    border-radius: 22px;
    background: var(--card-bg);
    overflow: hidden;
    box-shadow: 0 18px 40px rgba(0,0,0,0.12);
  }
  .card-shapes {
    position: absolute;
    inset: 0;
    width: 1000px;
    height: 560px;
  }
  .person {
    position: absolute;
    left: 420px;
    top: 128px;
    font-family: "Montserrat", sans-serif;
  }
  .person-name {
    margin: 0;
    font-size: 34px;
    line-height: 40px;
    font-weight: 600;
    letter-spacing: 0.5px;
    background: linear-gradient(90deg, var(--name-start), #c0324a 55%, var(--name-end));
    -webkit-background-clip: text;
    background-clip: text;
    color: transparent;
  }
  .person-role {
    margin: 6px 0 0 62px;
    font-size: 27px;
    line-height: 32px;
    font-weight: 500;
    color: var(--title);
    letter-spacing: 0.5px;
  }
  .contact-list {
    position: absolute;
    left: 292px;
    top: 318px;
    margin: 0;
    padding: 0;
    list-style: none;
    font-family: "Varela Round", sans-serif;
    font-size: 28px;
    color: var(--text);
  }
  .contact-item {
    display: flex;
    align-items: center;
    height: 40px;
    margin-bottom: 13px;
  }
  .contact-icon {
    width: 36px;
    height: 36px;
    border-radius: 7px;
    background: linear-gradient(135deg, var(--accent-red), var(--accent-magenta));
    margin-right: 16px;
    display: flex;
    align-items: center;
    justify-content: center;
    flex: none;
  }
  .contact-icon svg { width: 22px; height: 22px; }
</style>
</head>
<body>
  <div class="business-card">
    <svg class="card-shapes" viewBox="0 0 1000 560" aria-hidden="true">
      <path d="M0 0 H1000 V150 C920 60 800 -2 610 2 C300 8 140 300 112 560 H0 Z" fill="var(--band-dark)"/>
      <path d="M1000 166 C915 76 800 12 610 16 C312 22 158 306 128 560" fill="none" stroke="var(--accent-magenta)" stroke-width="7"/>
      <path d="M0 0 H236 C120 80 40 250 0 440 Z" fill="var(--accent-red)"/>
    </svg>

    <div class="person">
      <h1 class="person-name">RAFAEL MOREIRA</h1>
      <p class="person-role">GENERAL MANAGER</p>
    </div>

    <ul class="contact-list">
      <li class="contact-item">
        <span class="contact-icon">
          <svg viewBox="0 0 24 24"><path d="M6.6 10.8a15 15 0 0 0 6.6 6.6l2.2-2.2a1 1 0 0 1 1-.25 11.4 11.4 0 0 0 3.6.57 1 1 0 0 1 1 1V20a1 1 0 0 1-1 1A17 17 0 0 1 3 4a1 1 0 0 1 1-1h3.5a1 1 0 0 1 1 1c0 1.25.2 2.45.57 3.6a1 1 0 0 1-.25 1z" fill="#fff"/></svg>
        </span>
        (44) 9876-5410
      </li>
      <li class="contact-item">
        <span class="contact-icon">
          <svg viewBox="0 0 24 24"><rect x="3" y="6" width="18" height="12" rx="1.5" fill="#fff"/><path d="M3.5 7 L12 13 L20.5 7" fill="none" stroke="#b0124e" stroke-width="1.6"/></svg>
        </span>
        rafael@vitrix.com.br
      </li>
      <li class="contact-item">
        <span class="contact-icon">
          <svg viewBox="0 0 24 24"><path d="M6 4 L18 12 L12.5 13 L15.5 19 L13.3 20 L10.4 14 L6 18 Z" fill="#fff"/></svg>
        </span>
        www.vitrix.com.br
      </li>
      <li class="contact-item">
        <span class="contact-icon">
          <svg viewBox="0 0 24 24"><rect x="6" y="6" width="12" height="12" rx="2" fill="none" stroke="#fff" stroke-width="2"/></svg>
        </span>
        @vitrixbr
      </li>
    </ul>
  </div>
</body>
</html>
```